PLIVET Buck Slip: Request for Donations to our Program's Development Fund

We would like to create an invitation card/double sided pamplet (about 4x9 inches) to place in orthopaedics clinics and hand/mail out to potential donors about our research program, Westmere Study Group for Joint & Muscle Health. We have attached a copy of a design we've been working with but are looking for more of a professional touch.

Target Market(s)

Patients, Donors

Industry/Entity Type

Medical And Science

Font styles to use
Other font styles liked:
• Gothan Bold, Gotham Book, Gothan, Georgia, Serif, Sans Serif

Colors
ec1f27
f78f20
ffffff
000000
333333
5c5c5c
fbed22
fbee3d
ffc214

Requirements
Must have
• Please use the visual identity standards for guidance to help with colour choice and font selection (https://www.norvalenu.example/brand/system/files/1.0-logo-visual-identity_april2017.pdf)

```html
<!DOCTYPE html>
<html lang="en">
<head>
<meta charset="utf-8">
<title>PLIVET Buck Slip</title>
<link rel="stylesheet" href="https://fonts.googleapis.com/css2?family=Montserrat:wght@400;500;600;700&family=Lexend:wght@500;600&display=swap">
<style>
  :root{
    --red:#ec1f27;
    --orange:#f78f20;
    --yellow:#ffc214;
    --white:#ffffff;
    --black:#000000;
    --ink:#333333;
    --grey:#5c5c5c;
    --page:#e9e6e2;
  }
  *{box-sizing:border-box;margin:0;padding:0}
  html,body{width:1200px;height:1025px;overflow:hidden;background:var(--page)}
  body{font-family:"Montserrat",Arial,sans-serif;color:var(--ink);position:relative}
  .card{position:absolute;left:52px;width:1096px;height:486px;background:var(--white);overflow:hidden;box-shadow:0 3px 10px rgba(0,0,0,.18)}
  .card--front{top:16px}
  .card--back{top:522px}
  .front-art{position:absolute;inset:0}
  .quote{position:absolute;left:677px;top:58px;width:368px;font-size:21px;line-height:30.5px;color:var(--ink);text-align:justify;text-align-last:justify;letter-spacing:.6px}
  .quote-author{position:absolute;right:52px;top:214px;font-size:16px;font-weight:600;color:var(--red)}
  .brand{position:absolute;display:flex;align-items:center}
  .brand-name{font-family:"Lexend","Montserrat",sans-serif;font-weight:600;letter-spacing:-1px}
  .brand-divider{width:1px;align-self:stretch;margin:0 12px}
  .brand-unit{font-family:"Lexend","Montserrat",sans-serif;font-weight:500;line-height:1.2}
  .brand-unit span{display:block}
  .brand-unit .sub{letter-spacing:1.6px}
  .brand--front{left:32px;top:410px;height:56px;color:var(--white)}
  .brand--front .brand-name{font-size:44px}
  .brand--front .brand-divider{background:rgba(255,255,255,.8)}
  .brand--front .brand-unit{font-size:14.5px}
  .stripes{position:absolute;left:0;top:0}
  .brand--back{left:222px;top:36px;height:82px;color:var(--black)}
  .brand--back .brand-name{font-size:66px;color:var(--red);font-weight:700}
  .brand--back .brand-divider{background:#ccc;margin:0 20px}
  .brand--back .brand-unit{font-size:22.5px;line-height:1.18}
  .rule{position:absolute;left:0;top:119px;width:1096px;height:4px;background:linear-gradient(var(--orange) 0 50%,var(--grey) 50% 100%)}
  .mission{position:absolute;left:15px;top:126px;width:1065px;height:88px;background:var(--red);color:var(--white);text-align:center;padding-top:12px}
  .mission-lead{font-size:20.5px;font-weight:500;letter-spacing:.4px}
  .mission-pillars{font-size:21px;font-weight:400;letter-spacing:.8px;margin-top:6px;word-spacing:2px}
  .appeal{position:absolute;left:28px;top:232px;width:472px;font-size:19px;line-height:31px;text-align:justify}
  .appeal strong{color:var(--red);font-size:22px;font-weight:700}
  .contact{position:absolute;left:546px;top:230px;width:516px;height:114px;border-left:3px solid var(--red);text-align:right;font-size:19.5px;line-height:31px;color:var(--ink)}
  .contact-head{color:var(--red);font-weight:700;font-size:19.5px}
  .contact p{font-weight:500}
  .pledge{position:absolute;right:261px;top:393px;text-align:right;font-size:20.5px;line-height:31px}
  .pledge strong{font-weight:700}
  .pledge-link{color:var(--red);font-weight:700;font-size:20px;letter-spacing:.2px}
  .partners{position:absolute;left:898px;top:356px;width:180px;text-align:center}
  .partners-label{font-size:12.5px;font-weight:600;color:var(--ink)}
  .partner-marks{display:flex;justify-content:space-around;margin-top:14px}
  .partner-mark{width:44px;height:44px;border-radius:4px}
  .partner-mark--one{background:var(--yellow)}
  .partner-mark--two{background:#2a8fd6}
  .footer-band{position:absolute;left:0;bottom:0;width:1096px;height:24px;background:linear-gradient(var(--grey) 0 52%,var(--orange) 52% 100%)}
</style>
</head>
<body>

<section class="card card--front">
  <svg class="front-art" width="1096" height="486" viewBox="0 0 1096 486">
    <defs>
      <linearGradient id="sky" x1="0" y1="0" x2="1" y2="0">
        <stop offset="0" stop-color="#b9bdc2"/>
        <stop offset=".55" stop-color="#e4e5e7"/>
        <stop offset="1" stop-color="#ffffff"/>
      </linearGradient>
      <radialGradient id="hands" cx=".5" cy=".5" r=".55">
        <stop offset="0" stop-color="#3a2b22"/>
        <stop offset=".35" stop-color="#5a3e30"/>
        <stop offset=".6" stop-color="#d9a88f"/>
        <stop offset="1" stop-color="#d9a88f" stop-opacity="0"/>
      </radialGradient>
      <linearGradient id="swoop" x1="0" y1="0" x2="1" y2="1">
        <stop offset="0" stop-color="#e41f26"/>
        <stop offset=".6" stop-color="#ec3324"/>
        <stop offset="1" stop-color="#f0692a"/>
      </linearGradient>
    </defs>
    <rect width="1096" height="486" fill="url(#sky)"/>
    <ellipse role="img" aria-label="Cupped hands holding soil with a young green seedling" cx="390" cy="200" rx="340" ry="240" fill="url(#hands)"/>
    <path d="M0,80 C140,320 340,410 560,402 C780,394 975,305 1096,205 L1096,486 L0,486 Z" fill="url(#swoop)"/>
    <path d="M0,250 C200,420 500,470 760,440 C900,424 1010,380 1096,330 L1096,486 L0,486 Z" fill="#f15a2a" opacity=".35"/>
  </svg>
  <p class="quote">Modern medical advances have helped millions of people live longer, healthier lives. We owe these improvements to decades of investment in medical research</p>
  <p class="quote-author">- Dale Morrow</p>
  <div class="brand brand--front">
    <span class="brand-name">PLIVET</span>
    <span class="brand-divider"></span>
    <span class="brand-unit"><span>Westmere Study Group</span><span class="sub">for Joint &amp; Muscle Health</span></span>
  </div>
</section>

<section class="card card--back">
  <svg class="stripes" width="1096" height="24" viewBox="0 0 1096 24">
    <polygon points="216,6 965,6 958,14 209,14" fill="var(--red)"/>
    <polygon points="209,14 958,14 952,20 203,20" fill="var(--yellow)"/>
    <polygon points="985,6 1012,6 999,20 972,20" fill="var(--red)"/>
    <polygon points="1025,6 1052,6 1039,20 1012,20" fill="var(--red)"/>
    <polygon points="1065,6 1092,6 1079,20 1052,20" fill="var(--red)"/>
  </svg>
  <div class="brand brand--back">
    <span class="brand-name">PLIVET</span>
    <span class="brand-divider"></span>
    <span class="brand-unit"><span>Westmere Study Group</span><span class="sub">for Joint &amp; Muscle Health</span></span>
  </div>
  <div class="rule"></div>
  <div class="mission">
    <p class="mission-lead">We are passionate Clinicians and Educators focused on</p>
    <p class="mission-pillars">EMPOWERING PATIENTS &nbsp;•&nbsp; ADVANCING RESEARCH &nbsp;•&nbsp; IMPROVING CLINICAL CARE</p>
  </div>
  <p class="appeal"><strong>We need your help!</strong> Donations help run the PLIVET research program and without your support, it simply wouldn’t be possible.</p>
  <div class="contact">
    <p class="contact-head">To learn more, talk to your surgeon or contact us:</p>
    <p>Phone: 555-014-2290</p>
    <p>Email: jointstudy@norvalenu.example</p>
  </div>
  <div class="pledge">
    <p><strong>YES, I would like to help!</strong> Visit the following link:</p>
    <p class="pledge-link">https://give.norvalenu.example/medicine/PLIVET</p>
  </div>
  <div class="partners">
    <p class="partners-label">In partnership with:</p>
    <div class="partner-marks">
      <span class="partner-mark partner-mark--one"></span>
      <span class="partner-mark partner-mark--two"></span>
    </div>
  </div>
  <div class="footer-band"></div>
</section>

</body>
</html>
```